Business Card

THIS IS THE CARD INFORMATION
DEVELOPMENT I FINANCING I PROPERTY MANAGEMENT
DANIEL FERRÁN
3186 NE 74th Terrace
Coral Springs, FL 33076
Telephone I 855.274.6180
Facsimile I 855.274.6127
Industry/Entity Type
Business

```html
<!DOCTYPE html>
<html lang="en">
<head>
<meta charset="utf-8">
<title>Gómez Rivas &amp; Company – Business Card</title>
<link rel="stylesheet" href="https://fonts.googleapis.com/css2?family=Montserrat:wght@700&family=Nunito+Sans:wght@300&display=swap">
<style>
  :root {
    --page-bg: #ffffff;
    --card-light: #a8228c;
    --card-mid: #8c2178;
    --card-dark: #671f5b;
    --ink-white: #ffffff;
  }
  html, body {
    margin: 0;
    padding: 0;
    width: 1200px;
    height: 1000px;
    overflow: hidden;
    background: var(--page-bg);
  }
  .business-card {
    display: block;
    width: 1200px;
    height: 1000px;
  }
  .brand-name {
    font-family: "Montserrat", sans-serif;
    font-weight: 700;
    fill: var(--ink-white);
  }
  .contact-label,
  .contact-value {
    font-family: "Nunito Sans", sans-serif;
    font-weight: 300;
    font-size: 25px;
    fill: var(--ink-white);
    letter-spacing: 0.5px;
  }
  .stop-light { stop-color: var(--card-light); }
  .stop-mid { stop-color: var(--card-mid); }
  .stop-dark { stop-color: var(--card-dark); }
</style>
</head>
<body>
<svg class="business-card" viewBox="0 0 1200 1000" xmlns="http://www.w3.org/2000/svg">
  <defs>
    <radialGradient id="card-fill" cx="330" cy="220" r="820" gradientUnits="userSpaceOnUse">
      <stop offset="0" class="stop-light"/>
      <stop offset="0.5" class="stop-mid"/>
      <stop offset="1" class="stop-dark"/>
    </radialGradient>
    <linearGradient id="gloss-fill" x1="520" y1="202" x2="1087" y2="300" gradientUnits="userSpaceOnUse">
      <stop offset="0" stop-color="#ffffff" stop-opacity="0.2"/>
      <stop offset="1" stop-color="#ffffff" stop-opacity="0"/>
    </linearGradient>
    <clipPath id="card-shape">
      <path d="M109,202 H1027 A60,60 0 0 1 1087,262 V777 H169 A60,60 0 0 1 109,717 Z"/>
    </clipPath>
  </defs>

  <g class="card-face">
    <path class="card-background" fill="url(#card-fill)"
          d="M109,202 H1027 A60,60 0 0 1 1087,262 V777 H169 A60,60 0 0 1 109,717 Z"/>
    <path class="card-gloss" clip-path="url(#card-shape)" fill="url(#gloss-fill)"
          d="M520,202 Q660,290 1000,312 L1087,318 L1087,202 Z"/>
  </g>

  <g class="brand-lockup">
    <circle class="brand-dot" cx="262" cy="367" r="65" fill="none" stroke="var(--ink-white)" stroke-width="22"/>
    <text class="brand-name" x="362" y="387" font-size="101" textLength="643" lengthAdjust="spacingAndGlyphs">GÓMEZ RIVAS</text>
    <text class="brand-name" x="1004" y="433" font-size="46" text-anchor="end">&amp; COMPANY</text>
  </g>

  <g class="contact-block">
    <rect class="contact-frame" x="310.5" y="528.5" width="571" height="184" fill="none" stroke="var(--ink-white)" stroke-opacity="0.85" stroke-width="1"/>
    <text class="contact-label" x="362" y="579">WEB:</text>
    <text class="contact-value" x="475" y="577">WWW.GOMEZRIVAS.COM</text>
    <text class="contact-label" x="362" y="621">PHONE:</text>
    <text class="contact-value" x="475" y="621">111-111-111</text>
    <text class="contact-label" x="362" y="664">EMAIL:</text>
    <text class="contact-value" x="475" y="664">CONTACT@GOMEZRIVAS.COM</text>
  </g>
</svg>
</body>
</html>
```